Flyer-Design für private Musikakademie
Zielgruppe
Unsere Firma ist eine private Musikakademie für klassische Musik. Die Zielgruppe sind internationale Studenten und Publikum
Aufgabenstellung
Klassisch, elegant.
Wir benötigen einen Flyer im in zwei gefalteten A4 format (4 Seiten A5) für ein Festival in 2 Wochen.
Ausserdem benötigen wir einen stehenden Banner (ca. 2 m hoch) mit dem Hauptlogo und der Bezeichnung des Festivals.
Bitte kontaktieren Sie mich, falls Sie weiteres Bidmaterial, bzw. weitere Angaben benötigen. Das ist mein erstes aufgegebene Projekt hier.
Die Texteingabe ist in Deutsch/English. Meine Vorstellung wäre Deutsch etwas größer, English etwas versetzt darunter etwas kleiner, vielleicht kursiv, damit man es optisch gut auseinander halten kann

```html
<!DOCTYPE html>
<html lang="en">
<head>
<meta charset="utf-8">
<title>Music Academy Helle Töne Kassel – Festival Banner</title>
<link rel="stylesheet" href="https://fonts.googleapis.com/css2?family=Bebas+Neue&family=Tinos&display=swap">
<style>
  :root {
    --teal-top: #2aaebd;
    --teal-mid: #217880;
    --teal-bottom: #154a52;
    --white: #ffffff;
    --band-grey: #cfe0e3;
    --band-text: #1e4f57;
    --partner-pink: #e0308a;
    --partner-yellow: #f5e028;
    --ink: #1d1d1d;
    --shadow: 0 4px 8px rgba(0, 40, 50, 0.45);
  }
  * { margin: 0; padding: 0; box-sizing: border-box; }
  html, body { width: 1200px; height: 2400px; overflow: hidden; }
  body {
    position: relative;
    background: linear-gradient(180deg, var(--teal-top) 0%, var(--teal-mid) 50%, var(--teal-bottom) 100%);
    font-family: "Bebas Neue", "Oswald", sans-serif;
    color: var(--white);
  }
  .frame {
    position: absolute;
    left: 51px; top: 53px;
    width: 1093px; height: 2297px;
    border: 14px solid var(--white);
  }
  .emblem-space {
    position: absolute;
    left: 470px; top: 340px;
    width: 260px; height: 260px;
    border: 12px solid var(--white);
    box-shadow: var(--shadow);
  }
  .academy-name {
    position: absolute;
    left: 0; top: 845px; width: 1200px;
    text-align: center;
    line-height: 1;
    text-shadow: var(--shadow);
  }
  .academy-name span { display: block; }
  .academy-name .line-1 { font-size: 98px; height: 98px; }
  .academy-name .line-2 { font-size: 118px; height: 116px; margin-top: 4px; }
  .academy-name .line-3 { font-size: 140px; height: 140px; margin-top: 2px; }
  .rule {
    position: absolute;
    left: 110px; width: 978px; height: 8px;
    background: var(--white);
    box-shadow: var(--shadow);
  }
  .rule-top { top: 1339px; }
  .rule-bottom { top: 1538px; }
  .festival-title {
    position: absolute;
    left: 0; top: 1368px; width: 1200px;
    text-align: center;
    line-height: 1;
    text-shadow: var(--shadow);
  }
  .festival-title .place { display: block; font-size: 73px; }
  .festival-title .event { display: block; font-size: 78px; margin-top: 6px; }
  .sponsor-band {
    position: absolute;
    left: 65px; top: 1706px; width: 1065px; height: 77px;
    background: var(--band-grey);
    color: var(--band-text);
    font-size: 58px;
    line-height: 81px;
    text-align: center;
  }
  .partners {
    position: absolute;
    left: 65px; top: 1783px; width: 1065px; height: 242px;
    display: flex;
  }
  .partner {
    flex: 1;
    display: flex; align-items: center; justify-content: center;
    font-size: 58px;
    text-align: center;
    line-height: 1;
  }
  .partner-bow { background: var(--white); color: var(--ink); }
  .partner-friends { background: var(--partner-pink); color: var(--partner-yellow); font-size: 50px; padding: 0 30px; }
  .website {
    position: absolute;
    left: 0; top: 2178px; width: 1200px;
    text-align: center;
    font-family: "Tinos", "Times New Roman", serif;
    font-size: 44px;
    color: var(--white);
  }
</style>
</head>
<body>
  <div class="frame"></div>

  <div class="emblem-space"></div>

  <h1 class="academy-name">
    <span class="line-1">Music Academy</span>
    <span class="line-2">Helle Töne</span>
    <span class="line-3">Kassel</span>
  </h1>

  <div class="rule rule-top"></div>
  <h2 class="festival-title">
    <span class="place">Kassel – Klangwelt</span>
    <span class="event">International Festival and Competition</span>
  </h2>
  <div class="rule rule-bottom"></div>

  <div class="sponsor-band">Sponsored by</div>
  <div class="partners">
    <div class="partner partner-bow">Bogen Nord</div>
    <div class="partner partner-friends">Freunde der Kammermusik e.V.</div>
  </div>

  <p class="website">www.mahtk.de</p>
</body>
</html>
```